Screen Tides - Report on digital habits and attitudes

We are a research company and we have written a PowerPoint Report to present the results of a series of surveys conducted in the last three years. The research is about the "Screen Tides": people are facing the opportunities and challanges of their lives transformed by the digital technologies. We have investigated a number of topics through thousands of interviews and we've analyzed the data presented in the PowerPoint document.
We're not quite satisfied with the look and feel of the report: it looks too flat and boring, too "basic" to be presented as a professional work, yet being just that. We'd like you to upgrade the graphics and style of the report up to the level of a professional research product. The document still needs to be fully editable (either text and charts) but you can rearrange all the contents as you please, adding images, changing font and text size, colors and whatever you think is necessary to reach our goal.

Target Market(s)

Media covering digital issues
Marketing executives
Public institutions and policy makers

Industry/Entity Type

Market Research

Requirements
Must have
• The treats of a professional work
Fully editable within PowerPoint (either text and charts)
Nice to have
• Smart images
Original organization of the pages
Colors and graphics coherent with the corvalmeadow.it logo/website look and feel
Should not have
• PPT document over 30 MBytes
Images violating copyright

```html
<!DOCTYPE html>
<html lang="it">
<head>
<meta charset="utf-8">
<title>Screen Tides – Report</title>
<link href="https://fonts.googleapis.com/css2?family=Baloo+2:wght@600;700;800&family=Open+Sans:ital,wght@0,400;0,600;0,700;1,400;1,700&display=swap" rel="stylesheet">
<style>
:root{
  --orange:#f7952b;
  --orange-dark:#ea8218;
  --green:#8ea33a;
  --lime:#c9d86f;
  --ink:#3a3a3a;
  --text:#4a4a4a;
  --muted:#8a8a8a;
  --footer:#c6c6c6;
  --bg:#efeff1;
  --white:#ffffff;
}
*{margin:0;padding:0;box-sizing:border-box}
html,body{width:1200px;height:2393px;overflow:hidden;background:var(--bg)}
body{position:relative;font-family:"Open Sans",sans-serif;color:var(--text)}
.page{position:absolute;width:516px;height:728px;background:var(--white);box-shadow:0 3px 10px rgba(0,0,0,.18);overflow:hidden}
.p-cover{left:71px;top:82px}
.p-index{left:615px;top:82px}
.p-intro{left:71px;top:832px}
.p-fears{left:615px;top:832px}
.p-privacy{left:71px;top:1585px}
.p-attitudes{left:615px;top:1585px}
.abs{position:absolute}

.band{position:absolute;left:0;top:0;width:100%;height:66px;background:var(--orange)}
.band-title{position:absolute;left:34px;top:12px;font-family:"Baloo 2",sans-serif;font-weight:700;font-size:35px;line-height:44px;color:var(--white);text-shadow:1px 2px 2px rgba(0,0,0,.25)}

.foot{position:absolute;left:0;bottom:0;width:100%;height:44px;background:var(--footer)}
.foot-mark{position:absolute;left:6px;top:6px;width:32px;height:32px;background:var(--white);border-radius:3px}
.foot-mark::after{content:"";position:absolute;left:10px;top:10px;width:12px;height:12px;border-radius:50%;background:var(--orange)}
.foot-text{position:absolute;left:50px;top:14px;font-size:9.5px;font-weight:600;color:var(--white);letter-spacing:.1px}
.foot-num{position:absolute;right:28px;top:13px;font-size:11px;font-weight:700;color:var(--white)}

.copy{font-size:9.6px;line-height:15.2px;text-align:justify;color:var(--text)}
.copy p{margin-bottom:4px}
.copy .gap{margin-top:14px}
.copy b{color:var(--ink)}
.white-copy{color:var(--white);font-size:9.3px;line-height:15px;text-align:justify}

.section-bar{position:absolute;height:26px;background:var(--green);color:var(--white);font-weight:700;font-size:11px;line-height:26px;padding-left:14px}
.card{position:absolute;background:var(--white);box-shadow:0 2px 8px rgba(0,0,0,.14)}
.caption{position:absolute;font-size:7.4px;font-style:italic;color:var(--muted);text-align:center;border-top:1px solid #ddd;padding-top:3px}

.hbars{position:absolute}
.hrow{position:absolute;left:0;height:12px;width:100%}
.hlabel{position:absolute;top:0;font-size:7.2px;line-height:12px;color:#555;text-align:right;white-space:nowrap;overflow:hidden;text-overflow:ellipsis}
.hbar{position:absolute;top:0;height:12px;color:var(--white);font-size:8px;font-weight:600;line-height:12px;text-align:right;padding-right:6px}
.hbar.dark{background:var(--ink)}
.hbar.green{background:var(--green)}

.cover-logo{position:absolute;left:0;width:100%;top:48px;text-align:center}
.cover-logo .dot{display:block;width:22px;height:22px;border-radius:50%;background:var(--orange);margin:0 auto 10px}
.cover-logo .name{font-size:11px;font-weight:700;letter-spacing:3px;color:var(--ink)}
.cover-photo{position:absolute;left:0;top:217px;width:516px;height:360px;background:linear-gradient(125deg,#cfd6dc 0%,#9aa7b2 35%,#55606b 70%,#2e3238 100%)}
.cover-block{position:absolute;left:27px;top:165px;width:226px;height:563px;background:var(--orange)}
.cover-title{position:absolute;left:42px;top:345px;font-family:"Baloo 2",sans-serif;font-weight:700;color:var(--white);font-size:31px;line-height:32px}
.cover-title .lead{display:block;margin-bottom:28px}

.toc{position:absolute;left:6px;top:195px;width:463px;height:351px;background:var(--white);box-shadow:0 2px 10px rgba(0,0,0,.12);padding:26px 18px 0 25px}
.toc-row{display:flex;height:37.2px;align-items:center;border-bottom:1px solid #bbb;font-weight:700;font-size:14px;color:var(--ink)}
.toc-row:last-child{border-bottom:none}
.toc-row .ch{width:307px;height:100%;display:flex;align-items:center;border-right:1px solid #bbb}
.toc-row .pg{flex:1;text-align:center}

.callout{position:absolute;left:269px;top:625px;width:247px;height:44px;background:var(--green);color:var(--white);font-weight:700;font-size:9.6px;line-height:13px;padding:8px 10px}

svg text{font-family:"Open Sans",sans-serif}
</style>
</head>
<body>

<section class="page p-cover">
  <div class="cover-logo"><span class="dot"></span><span class="name">CORVALMEADOW</span></div>
  <div class="cover-photo" role="img" aria-label="Foto: mani che usano un tablet con una galleria di immagini davanti a un portatile"></div>
  <div class="cover-block"></div>
  <h1 class="cover-title"><span class="lead">OST</span>Osservatorio<br>Screen<br>Tides</h1>
</section>

<section class="page p-index">
  <div class="band"><h2 class="band-title">Indice</h2></div>
  <div class="toc">
    <div class="toc-row"><span class="ch">Capitolo 1</span><span class="pg">01</span></div>
    <div class="toc-row"><span class="ch">Capitolo 1</span><span class="pg">04</span></div>
    <div class="toc-row"><span class="ch">Capitolo 1</span><span class="pg">10</span></div>
    <div class="toc-row"><span class="ch">Capitolo 1</span><span class="pg">15</span></div>
    <div class="toc-row"><span class="ch">Capitolo 1</span><span class="pg">20</span></div>
    <div class="toc-row"><span class="ch">Capitolo 1</span><span class="pg">24</span></div>
    <div class="toc-row"><span class="ch">Capitolo 1</span><span class="pg">28</span></div>
    <div class="toc-row"><span class="ch">Capitolo 1</span><span class="pg">30</span></div>
  </div>
  <footer class="foot"><span class="foot-mark"></span><span class="foot-text">SCREEN TIDES | dicembre 2020 | © Corvalmeadow 2020</span><span class="foot-num">2</span></footer>
</section>

<section class="page p-intro">
  <div class="band"><h2 class="band-title">Introduzione</h2></div>
  <div class="copy abs" style="left:36px;top:97px;width:218px">
    <p>Il digitale ha cambiato il mondo a un livello di profondità di cui non siamo ancora pienamente consapevoli.</p>
    <p>E’ facile riconoscere le manifestazioni del digitale nei <b>comportamenti delle persone</b> e notare come ha formato nuove abitudini e ritualità quotidiane.</p>
    <p>Non è altrettanto immediato comprendere quanto il digitale abbia modificato il <b>mondo interiore</b> e abbia inciso sul senso dell’identità, sulle emozioni in gioco nelle relazioni, su affetti e sessualità, sul modo di concepire la società, i diritti e la libertà personale.</p>
    <p class="gap">L’obiettivo di questo lavoro di ricerca è raccontare la struttura e l’evoluzione di alcuni atteggiamenti di fondo che influenzano i comportamenti quotidiani legati alle tecnologie digitali. Le informazioni sono ricavate dalle dichiarazioni di campioni di individui chiamati a riflettere sull’<b><i>ambiente connesso</i></b>, cioè l’insieme di tutte le relazioni e attività che si possono svolgere grazie alla Rete e, più in generale, grazie a tutte le innovazioni introdotte dagli strumenti e dai servizi digitali.</p>
    <p class="gap">L’analisi indaga le dinamiche cognitive e psicologiche che originano i comportamenti e descrive gli orientamenti di base sottostanti alle scelte – talvolta inconsapevoli – che danno forma alla dimensione digitale della vita. Questa, infatti, può assumere una configurazione molto diversa dalla dimensione della vita di prima (a cui ci riferimento col termine «naturale», intendendo con questo la</p>
  </div>
  <div class="copy abs" style="left:269px;top:97px;width:218px">
    <p>vita non mediata dagli strumenti dell’ICT): persone introverse nella vita naturale possono avere una vita digitale ricca di relazioni e attività, così come persone di orientamento liberale nella vita naturale possono assumere atteggiamenti reazionari o anarchici nella dimensione digitale della vita.</p>
    <p class="gap">La recente esperienza del lockdown per il Covid-19 ha <b>accelerato l’evoluzione del fenomeno</b> e ha esasperato alcuni aspetti della <b>dimensione digitale della vita</b>. Per alcuni mesi il mondo è stato un inedito e prezioso laboratorio di psicologia sociale: le forme digitali delle relazioni personali e sociali hanno prevalso e sostituito quelle della vita naturale e hanno generato riflessioni non astratte ma elaborate sulla base delle esperienze vissute.</p>
    <p>Per questi motivi Corvalmeadow ha prodotto le analisi dei dati e ha anticipato l’uscita di questo Rapporto, anche se il lavoro ha l’obiettivo di seguire i fenomeni per un tempo più lungo, di almeno un decennio.</p>
    <p class="gap">Le innovazioni dell’epoca moderna hanno generato benessere diffuso: dalla medicina all’elettricità, dalla diffusione della conoscenza alla produzione e distribuzione dei prodotti alimentari.</p>
    <p>La domanda che ci poniamo oggi è relativa alle tecnologie digitali: ci renderanno la vita più facile, la convivenza più pacifica, ci daranno una salute migliore?</p>
  </div>
  <div class="callout">In definitiva, il digitale ci renderà più felici?</div>
  <footer class="foot"><span class="foot-mark"></span><span class="foot-text">SCREEN TIDES | dicembre 2020 | © Corvalmeadow 2020</span><span class="foot-num">3</span></footer>
</section>

<section class="page p-fears">
  <div class="band" style="height:176px"><h2 class="band-title">Le paure</h2></div>
  <div class="white-copy abs" style="left:30px;top:75px;width:460px">
    Il digitale può fare paura per le conseguenze che produce nelle capacità cognitive, nelle relazioni personali e sociali, fino a quelle internazionali. Molti non conoscono cosa c’è dietro e da dove vengono certe <b><i>magie della tecnologia</i></b>, alle quali ci siamo abituati e che non ci meravigliano più ma rimangono in gran parte incomprensibili.<br>
    Inoltre, certi racconti sulle sorveglianza digitale e sui nuovi poteri che emergono dai dati ispirano un senso di sospetto condiviso da un’ampia maggioranza di individui.
  </div>
  <div class="card" style="left:26px;top:178px;width:466px;height:175px"></div>
  <div class="section-bar" style="left:0;top:184px;width:474px;padding-left:30px">Le paure e i sospetti</div>
  <div class="hbars" style="left:30px;top:222px;width:460px;height:125px">
    <div class="hrow" style="top:0"><span class="hlabel" style="right:128px;width:330px">Nell’ambiente connesso è più facile manipolare le persone</span><span class="hbar dark" style="left:336px;width:91px">80%</span></div>
    <div class="hrow" style="top:15px"><span class="hlabel" style="right:128px;width:330px">I ragazzi hanno notevoli problemi di socializzazione a causa del digitale</span><span class="hbar dark" style="left:336px;width:88px">77%</span></div>
    <div class="hrow" style="top:30px"><span class="hlabel" style="right:128px;width:330px">Alcuni servizi sanno tutto di noi: chi vediamo, cosa facciamo, cosa scriviamo e diciamo, anche quando non siamo online</span><span class="hbar dark" style="left:336px;width:86px">75%</span></div>
    <div class="hrow" style="top:45px"><span class="hlabel" style="right:128px;width:330px">I dispositivi che utilizzo mandano continuamente dati su di me a organizzazioni di cui ignoro l’esistenza</span><span class="hbar dark" style="left:336px;width:81px">71%</span></div>
    <div class="hrow" style="top:60px"><span class="hlabel" style="right:128px;width:330px">Le notizie online ci fanno perdere la capacità di distinguere il vero dal falso</span><span class="hbar dark" style="left:336px;width:80px">70%</span></div>
    <div class="hrow" style="top:75px"><span class="hlabel" style="right:128px;width:330px">Il digitale diminuisce la capacità di apprendimento a tutte le età</span><span class="hbar dark" style="left:336px;width:48px">42%</span></div>
    <div class="hrow" style="top:90px"><span class="hlabel" style="right:128px;width:330px">Le democrazie sono a rischio a causa della diffusione dell’online</span><span class="hbar dark" style="left:336px;width:40px">35%</span></div>
    <div class="hrow" style="top:105px"><span class="hlabel" style="right:128px;width:330px">Prossimamente ci sarà una guerra cibernetica fra Stati</span><span class="hbar dark" style="left:336px;width:38px">33%</span></div>
  </div>
  <div class="caption" style="left:40px;top:368px;width:436px">Incidenza sul totale campione dei Top2Box di accordo, in una scala a 5 passi (1.017 casi a novembre 2020)</div>
  <div class="copy abs" style="left:32px;top:394px;width:220px">
    <p>Il sospetto che il flusso di informazioni generato dalle tecnologie sia utilizzato con finalità di <b>controllo o manipolazione</b> è molto diffuso e riguarda otto individui sui dieci.</p>
    <p>Il 77% si dichiara d’accordo con l’affermazione secondo la quale il digitale crea <b>problemi di socialità</b> nei ragazzi e il dato aumenta tra le</p>
  </div>
  <div class="copy abs" style="left:266px;top:394px;width:220px">
    <p>persone oltre i 54 anni di età. Così come tra i meno giovani trova conferma l’idea, già piuttosto diffusa, che il digitale diminuisca le <b>capacità di apprendimento</b>.</p>
    <p>Le paure sulle conseguenze politiche e sociali del digitale sono più contenute ma riguardano pur sempre un terzo della popolazione.</p>
  </div>
  <div class="section-bar" style="left:0;top:514px;width:476px;padding-left:32px">Il trend dell’indice di paura</div>
  <svg class="abs" style="left:0;top:0" width="516" height="728" viewBox="0 0 516 728" aria-label="Andamento dell’indice di paura">
    <path d="M88 606 C130 602,150 600,173 595 S230 565,261 561 S320 588,348 589 S410 584,435 582" fill="none" stroke="#999" stroke-width="1.2" stroke-dasharray="2 2"/>
    <g fill="#aaa"><circle cx="88" cy="606" r="3"/><circle cx="173" cy="595" r="3"/><circle cx="261" cy="561" r="3"/><circle cx="348" cy="589" r="3"/><circle cx="435" cy="582" r="3"/></g>
    <g font-size="9.5" fill="#555" text-anchor="middle"><text x="88" y="624">58%</text><text x="175" y="612">59%</text><text x="262" y="578">62%</text><text x="349" y="603">60%</text><text x="436" y="596">60%</text></g>
    <line x1="40" y1="638" x2="480" y2="638" stroke="#ddd"/>
    <g font-size="9.5" fill="#999" text-anchor="middle"><text x="88" y="650">feb 19</text><text x="175" y="650">ott 19</text><text x="262" y="650">feb 20</text><text x="349" y="650">mag 20</text><text x="436" y="650">nov 20</text></g>
    <text x="258" y="664" font-size="7.4" font-style="italic" fill="#888" text-anchor="middle">L’indice di paura è ottenuto come media semplice dei Top2Box delle otto voci analizzate</text>
  </svg>
  <footer class="foot"><span class="foot-mark"></span><span class="foot-text">SCREEN TIDES | dicembre 2020 | © Corvalmeadow 2020</span><span class="foot-num">5</span></footer>
</section>

<section class="page p-privacy">
  <div class="band"><h2 class="band-title" style="left:26px">Data&amp;Privacy</h2></div>
  <div class="copy abs" style="left:32px;top:82px;width:222px">
    <p>Il tema del tracciamento dei dati personali per fini commerciali si conferma in tutte le rilevazioni una pratica fastidiosa per la maggioranza degli intervistati, con una quota variabile tra il 57 e il 62%.</p>
    <p>Si nota però una leggera e progressiva diminuzione dell’attenzione degli italiani su questo aspetto. Forse perché, essendo ormai una prassi consolidata, la si ritiene sempre più inevitabile e sempre meno urgente.</p>
  </div>
  <div class="copy abs" style="left:266px;top:82px;width:222px">
    <p>che per godere dei vantaggi derivanti dalla tecnologia sia necessario rinunciare in parte alle propria privacy.</p>
  </div>
  <div class="section-bar" style="left:4px;top:252px;width:252px">Tracciamento per fini commerciali</div>
  <div class="section-bar" style="left:266px;top:136px;width:250px">La tecnologia toglie, la tecnologia dà</div>
  <div class="copy abs" style="left:32px;top:436px;width:222px">
    <p>Come già osservato a livello generale, durante la prima ondata di Covid-19 l’attenzione al tema della privacy è aumentata significativamente e le posizioni degli italiani si sono estremizzate e polarizzate. Se da un lato aumenta il sospetto che i dati personali siano utilizzati ridefinire gli equilibri geo-politici tra Stati e che il tracciamento possa essere un pericolo per la società, dall’altro si nota che l’emergenza Covid ha stimolato un atteggiamento più «benevolo» ed «equilibrato» verso la tecnologia, eliminando alcune resistenze al tracciamento e agevolando l’accettazione del compromesso</p>
  </div>
  <div class="copy abs" style="left:266px;top:308px;width:222px">
    <p>L’effetto Covid sull’atteggiamento delle persone in merito al tema tracciamento e privacy è stato però di breve periodo: già a Novembre 2020, in piena seconda ondata, l’attenzione è tornata ai livelli pre pandemia, livelli che comunque mostravano una diffusa preoccupazione su tutti i piani (geo-politica, società, libertà individuale) accompagnata da una altrettanto diffusa consapevolezza dell’equilibrio e del bilanciamento (il digitale toglie privacy ma restituisce servizi).</p>
  </div>
  <div class="section-bar" style="left:266px;top:487px;width:250px">Tracciamento per fini geo-politici</div>
  <svg class="abs" style="left:0;top:0" width="516" height="728" viewBox="0 0 516 728" aria-label="Grafici a bolle su tracciamento e privacy">
    <defs>
      <filter id="soft" x="-50%" y="-50%" width="200%" height="200%"><feDropShadow dx="0" dy="1" stdDeviation="1.2" flood-opacity=".3"/></filter>
    </defs>
    <g stroke="#cfcfcf" stroke-width="1" fill="none">
      <polyline points="46,338 91,335 136,338 181,346 226,345"/>
      <polyline points="294,234 339,238 386,245 432,213 478,236"/>
      <polyline points="294,590 339,583 386,577 432,556 478,583"/>
    </g>
    <g fill="var(--lime)" stroke="#fff" stroke-width="2" filter="url(#soft)">
      <circle cx="46" cy="338" r="12"/><circle cx="91" cy="335" r="12"/><circle cx="136" cy="338" r="12"/><circle cx="181" cy="346" r="12"/><circle cx="226" cy="345" r="12"/>
      <circle cx="294" cy="234" r="12"/><circle cx="339" cy="238" r="12"/><circle cx="386" cy="245" r="12"/><circle cx="432" cy="213" r="12"/><circle cx="478" cy="236" r="12"/>
      <circle cx="294" cy="590" r="12"/><circle cx="339" cy="583" r="12"/><circle cx="386" cy="577" r="12"/><circle cx="432" cy="556" r="12"/><circle cx="478" cy="583" r="12"/>
    </g>
    <g font-size="7.8" fill="#444" text-anchor="middle">
      <text x="46" y="341">60%</text><text x="91" y="338">62%</text><text x="136" y="341">60%</text><text x="181" y="349">57%</text><text x="226" y="348">58%</text>
      <text x="294" y="237">45%</text><text x="339" y="241">43%</text><text x="386" y="248">41%</text><text x="432" y="216">52%</text><text x="478" y="239">44%</text>
      <text x="294" y="593">40%</text><text x="339" y="586">42%</text><text x="386" y="580">44%</text><text x="432" y="559">50%</text><text x="478" y="586">43%</text>
    </g>
    <g stroke="#ddd"><line x1="30" y1="392" x2="250" y2="392"/><line x1="276" y1="272" x2="498" y2="272"/><line x1="276" y1="628" x2="498" y2="628"/></g>
    <g font-size="9" fill="#999" text-anchor="middle">
      <text x="46" y="405">feb 19</text><text x="91" y="405">ott 19</text><text x="136" y="405">feb 20</text><text x="181" y="405">mag 20</text><text x="226" y="405">nov 20</text>
      <text x="294" y="285">feb 19</text><text x="339" y="285">ott 19</text><text x="386" y="285">feb 20</text><text x="432" y="285">mag 20</text><text x="478" y="285">nov 20</text>
      <text x="294" y="641">feb 19</text><text x="339" y="641">ott 19</text><text x="386" y="641">feb 20</text><text x="432" y="641">mag 20</text><text x="478" y="641">nov 20</text>
    </g>
  </svg>
  <footer class="foot"><span class="foot-mark"></span><span class="foot-text">SCREEN TIDES | dicembre 2020 | © Corvalmeadow 2020</span><span class="foot-num">10</span></footer>
</section>

<section class="page p-attitudes">
  <div class="band" style="height:243px"><h2 class="band-title" style="top:16px">Gli atteggiamenti di base</h2></div>
  <div class="white-copy abs" style="left:36px;top:78px;width:452px">
    Il digitale è ormai parte della nostra quotidianità ed è diventato un aspetto imprescindibile della nostra vita personale e di cittadini all’interno di una comunità. La maggioranza degli italiani online ormai non riesce più a concepire la sua vita senza i servizi digitali (fino ad esserne addirittura «ossessionata») e c’è un ampio consenso sulla necessità che lo stato promuova iniziative per superare il <b><i>digital divide</i></b> e garantire uguali condizioni di accesso ai servizi digitali. È indubbio infatti che i servizi e le opportunità offerte dal digitale abbiano contribuito a migliorare e semplificare la nostra vita (ne sono convinti 3 italiani su 4).<br>
    Quando però ci si sposta dal livello dei servizi offerti dal digitale ad altri aspetti come la libertà individuale, le relazioni e la convivenza tra individui, i benefici offerti dal digitale risultano decisamente meno evidenti ai più e la rivoluzione digitale non convince del tutto.
  </div>
  <div class="card" style="left:32px;top:250px;width:460px;height:144px"></div>
  <div class="section-bar" style="left:28px;top:250px;width:444px">Atteggiamenti di base</div>
  <div class="hbars" style="left:36px;top:294px;width:456px;height:100px">
    <div class="hrow" style="top:0"><span class="hlabel" style="right:144px;width:300px">Almeno metà delle persone sono ossessionate dalla necessità di essere sempre connesse</span><span class="hbar green" style="left:317px;width:109px">79%</span></div>
    <div class="hrow" style="top:14px"><span class="hlabel" style="right:144px;width:300px">L’accesso online ai servizi digitali deve essere un diritto garantito dallo Stato</span><span class="hbar green" style="left:317px;width:105px">76%</span></div>
    <div class="hrow" style="top:28px"><span class="hlabel" style="right:144px;width:300px">Il digitale ha migliorato/ semplificato la mia vita</span><span class="hbar green" style="left:317px;width:101px">73%</span></div>
    <div class="hrow" style="top:42px"><span class="hlabel" style="right:144px;width:300px">Non riesco più a concepire la mia vita senza i servizi digitali</span><span class="hbar green" style="left:317px;width:75px">54%</span></div>
    <div class="hrow" style="top:56px"><span class="hlabel" style="right:144px;width:300px">Il digitale ha aumentato la mia libertà</span><span class="hbar green" style="left:317px;width:62px">45%</span></div>
    <div class="hrow" style="top:70px"><span class="hlabel" style="right:144px;width:300px">Il digitale mi fa vivere meglio le relazioni con le altre persone</span><span class="hbar green" style="left:317px;width:55px">40%</span></div>
    <div class="hrow" style="top:84px"><span class="hlabel" style="right:144px;width:300px">Il digitale ha migliorato la convivenza tra le persone</span><span class="hbar green" style="left:317px;width:52px">38%</span></div>
  </div>
  <div class="caption" style="left:40px;top:406px;width:440px">Incidenza sul totale campione dei Top2Box di accordo, in una scala a 5 passi (1.017 casi a novembre 2020)</div>
  <div class="copy abs" style="left:36px;top:432px;width:220px">
    <p>Nel corso del tempo non si osservano variazioni significative negli atteggiamenti di base sul digitale: 2 italiani su 3 sono convinti</p>
  </div>
  <div class="copy abs" style="left:266px;top:432px;width:220px">
    <p>che il digitale sia una dimensione fondamentale della vita e 1 su 2 che la sua diffusione produca benefici in diversi ambiti.</p>
  </div>
  <div class="section-bar" style="left:0;top:483px;width:472px;padding-left:38px">Il trend delle convinzioni di base sul digitale</div>
  <svg class="abs" style="left:0;top:0" width="516" height="728" viewBox="0 0 516 728" aria-label="Andamento delle convinzioni di base sul digitale">
    <g font-size="9" font-style="italic" fill="#555" text-anchor="end">
      <text x="120" y="548">Il digitale è una</text><text x="120" y="559" font-weight="700">necessità*</text>
      <text x="120" y="580">Il digitale</text><text x="120" y="591" font-weight="700">migliora la vita**</text>
    </g>
    <polyline points="160,554 230,557 301,554 372,550 442,551" fill="none" stroke="#555" stroke-width="1.2" stroke-dasharray="1.5 2"/>
    <polyline points="160,574 230,578 301,571 372,572 442,575" fill="none" stroke="#999" stroke-width="1.2" stroke-dasharray="1.5 2"/>
    <g fill="var(--green)"><circle cx="160" cy="554" r="3"/><circle cx="230" cy="557" r="3"/><circle cx="301" cy="554" r="3"/><circle cx="372" cy="550" r="3"/><circle cx="442" cy="551" r="3"/></g>
    <g fill="var(--lime)"><circle cx="160" cy="574" r="3"/><circle cx="230" cy="578" r="3"/><circle cx="301" cy="571" r="3"/><circle cx="372" cy="572" r="3"/><circle cx="442" cy="575" r="3"/></g>
    <g font-size="9.5" fill="#444" text-anchor="middle">
      <text x="160" y="545">62%</text><text x="230" y="548">59%</text><text x="301" y="545">62%</text><text x="372" y="541">66%</text><text x="442" y="542">65%</text>
      <text x="160" y="591">50%</text><text x="230" y="595">46%</text><text x="301" y="588">52%</text><text x="372" y="589">51%</text><text x="442" y="592">49%</text>
    </g>
    <line x1="130" y1="611" x2="480" y2="611" stroke="#ddd"/>
    <g font-size="9" fill="#999" text-anchor="middle"><text x="160" y="624">feb 19</text><text x="230" y="624">nov 19</text><text x="301" y="624">feb 20</text><text x="372" y="624">mag 20</text><text x="442" y="624">nov 20</text></g>
    <line x1="40" y1="646" x2="480" y2="646" stroke="#ddd"/>
    <g font-size="5" font-style="italic" fill="#888" text-anchor="middle">
      <text x="260" y="654">*Indice ottenuto come media semplice dei Top2Box delle voci sulla necessità dei servizi digitali e dell’accesso garantito</text>
      <text x="260" y="661">**Indice ottenuto come media semplice dei Top2Box delle voci sul miglioramento della vita grazie al digitale</text>
    </g>
  </svg>
  <footer class="foot"><span class="foot-mark"></span><span class="foot-text">SCREEN TIDES | dicembre 2020 | © Corvalmeadow 2020</span><span class="foot-num">11</span></footer>
</section>

</body>
</html>
```